Tolvik cards

I want a simple business card that pops.
Logo on one side.
On side two i want.
"Are you thinking about a new building on your property, or renovating an existing structure? Contact".....
Owners Name: Gary Pellman
Owners Phone number: 555-209-4176
Address:4716 Copper Fern RD, Ashvale, PA 16001
Committed to Quality, Service, and Integrity

```html
<!DOCTYPE html>
<html lang="en">
<head>
<meta charset="utf-8">
<title>Tolvik Builders LLC – Business Card</title>
<link rel="stylesheet" href="https://fonts.googleapis.com/css2?family=Archivo:wght@800&family=Arimo:ital,wght@0,400;0,700;1,700&display=swap">
<style>
  :root {
    --backdrop: #5b5b5b;
    --paper: #ffffff;
    --brown-ink: #4a3220;
    --brown-band: #3f2a1a;
    --tan-line: #a68d74;
    --tan-name: #a99880;
    --white: #ffffff;
    --back-mid: #7a5c40;
    --back-dark: #4a2f19;
    --copper: #b07a4e;
  }
  * { box-sizing: border-box; margin: 0; padding: 0; }
  html, body {
    width: 1200px; height: 1200px; overflow: hidden;
    background: var(--backdrop);
  }
  .card { position: absolute; overflow: hidden; }

  /* Front */
  .card--front { left: 266px; top: 158px; width: 688px; height: 393px; background: var(--paper); }
  .question {
    position: absolute; top: 30px; left: 0; right: 0;
    text-align: center;
    font-family: "Arimo", Arial, sans-serif; font-style: italic; font-weight: 700;
    font-size: 20px; line-height: 24px; color: var(--brown-ink);
  }
  .brand__square {
    position: absolute; left: 145px; top: 98px; width: 100px; height: 100px;
    background: var(--brown-ink);
  }
  .brand__main, .brand__sub {
    position: absolute; left: 277px;
    font-family: "Archivo", Arial, sans-serif; font-weight: 800;
    color: var(--brown-ink); line-height: 1; white-space: nowrap;
  }
  .brand__main { top: 126px; font-size: 60px; letter-spacing: -1px; }
  .brand__sub { top: 184px; font-size: 19px; letter-spacing: 2px; padding-left: 2px; }
  .rule { position: absolute; left: 0; right: 0; top: 239px; height: 4px; background: var(--tan-line); }
  .band {
    position: absolute; left: 0; right: 0; top: 247px; bottom: 0;
    background: var(--brown-band);
  }
  .owner {
    position: absolute; left: 51px; top: 41px;
    font-family: "Archivo", Arial, sans-serif; font-weight: 800;
    font-size: 27px; line-height: 30px; color: var(--tan-name); letter-spacing: 0.5px;
    white-space: nowrap;
  }
  .divider { position: absolute; left: 316px; top: 32px; width: 1px; height: 54px; background: var(--tan-name); }
  .contact {
    position: absolute; left: 333px; top: 36px;
    font-family: "Arimo", Arial, sans-serif; font-size: 16px; line-height: 23px; color: var(--white);
    white-space: nowrap;
  }
  .contact__phone { display: flex; align-items: center; gap: 9px; }
  .contact__phone svg { width: 14px; height: 14px; }
  .tagline {
    position: absolute; left: 0; right: 0; top: 106px; text-align: center;
    font-family: "Arimo", Arial, sans-serif; font-size: 18px; color: var(--white);
  }

  /* Back */
  .card--back { left: 260px; top: 651px; width: 692px; height: 395px; }
  .back-pattern {
    position: absolute; inset: 0;
    background:
      radial-gradient(ellipse 55% 65% at 50% 50%, rgba(168,150,120,0.95), rgba(122,92,64,0.6) 55%, rgba(74,47,25,0) 100%),
      linear-gradient(90deg, var(--back-dark) 0%, var(--back-mid) 35%, var(--copper) 80%, var(--back-dark) 100%);
  }
  .back-mark {
    position: absolute; left: 596px; top: 296px;
    display: flex; align-items: center; gap: 6px;
    font-family: "Archivo", Arial, sans-serif; font-weight: 800; font-size: 16px; color: var(--white);
  }
  .back-mark__square { width: 12px; height: 12px; background: var(--white); }
</style>
</head>
<body>
  <section class="card card--front">
    <p class="question">Are you thinking about a new building on your property,<br>or renovating an existing structure?</p>
    <span class="brand__square"></span>
    <span class="brand__main">TOLVIK</span>
    <span class="brand__sub">BUILDERS LLC</span>
    <div class="rule"></div>
    <div class="band">
      <p class="owner">GARY PELLMAN</p>
      <span class="divider"></span>
      <div class="contact">
        <p class="contact__phone">
          <svg viewBox="0 0 24 24" aria-hidden="true"><path fill="#a99880" d="M6.6 10.8a15.2 15.2 0 0 0 6.6 6.6l2.2-2.2a1 1 0 0 1 1-.25 11.4 11.4 0 0 0 3.6.57 1 1 0 0 1 1 1V20a1 1 0 0 1-1 1A17 17 0 0 1 3 4a1 1 0 0 1 1-1h3.5a1 1 0 0 1 1 1c0 1.25.2 2.45.57 3.57a1 1 0 0 1-.25 1z"/></svg>
          555-209-4176
        </p>
        <p>4716 Copper Fern RD, Ashvale, PA 16001</p>
      </div>
      <p class="tagline">Committed to Quality, Service, and Integrity</p>
    </div>
  </section>

  <section class="card card--back">
    <div class="back-pattern" role="img" aria-label="Repeating embossed brand-mark pattern in bronze and copper tones"></div>
    <div class="back-mark"><span class="back-mark__square"></span>TOLVIK</div>
  </section>
</body>
</html>
```